Small Ecommerce Styled Site to Sell / Lease Domain Names

We have a small portfolio of 100+ domain names that we would like to offer for sale or lease via a web site. Along the lines of http://www.velramarkets.com/searchdomain.html?priceChoice=2&sort=leasing_desc

We would like initially a 4 page design, listing page (as site referenced above), domain info page (Universal Domain Name Landing Page with form) and checkout a page and About Us Page

We do not want a replica of the site listed, please use it as a guide only, we are looking for a fresh design, in similar concept web 2.0

Our Colours are #351a41 (Main) - #ffca27 (Secondary) all other colours must compliment those 2.
Updates

Domain Landing Page:  I am sorry I was not clear about expectations, however we would like a domain landing page that would be the default holding page for a domain name.

For some examples of what I mean please see:
https://www.pobexhub.com.au/guest-articles/7626-domain-for-sale-landing-pages.html
http://dev.quillterbrokers.com/blog/2013/09/sales-only-landers-and-buy-it-now-2/

Industry/Entity Type

Domain

Font styles to use
Sans Serif

```html
<!DOCTYPE html>
<html lang="en">
<head>
<meta charset="utf-8">
<title>Lesyra Domains</title>
<link rel="stylesheet" href="https://fonts.googleapis.com/css2?family=Open+Sans:wght@400;600;700;800&display=swap">
<style>
:root{
  --purple:#351a41;
  --purple-deep:#26112f;
  --yellow:#ffca27;
  --ink:#333;
  --muted:#777;
  --line:#e3e3e3;
  --paper:#fff;
  --soft:#f3f3f5;
}
*{box-sizing:border-box;margin:0;padding:0}
html,body{width:1200px;height:2368px;overflow:hidden}
body{font-family:"Open Sans",Arial,sans-serif;color:var(--ink);background:var(--paper);font-size:13px}
.wrap{width:1000px;margin:0 auto;position:relative;height:100%}
.topbar{height:24px;background:var(--purple);color:#d9cfe0;font-size:10px}
.topbar .wrap{display:flex;justify-content:space-between;align-items:center}
.topbar nav span{margin-left:16px}
.header{height:86px;border-bottom:1px solid var(--line)}
.header .wrap{display:flex;justify-content:space-between;align-items:center}
.brand{font-size:30px;font-weight:800;color:var(--purple);letter-spacing:-.5px}
.mainnav{display:flex;gap:4px}
.mainnav a{font-size:14px;color:var(--ink);padding:8px 12px;text-decoration:none}
.mainnav a.active{background:var(--yellow);color:var(--purple);font-weight:600}
.hero{height:450px;background:linear-gradient(#ececef,#f7f7f8)}
.hero h1{position:absolute;left:40px;top:62px;font-size:33px;font-weight:600;color:var(--purple);letter-spacing:-.3px;white-space:nowrap}
.hero h2{position:absolute;left:40px;top:108px;font-size:19px;font-weight:600;color:var(--purple);white-space:nowrap}
.search{position:absolute;left:40px;top:200px;width:540px;height:50px;display:flex;border:2px solid var(--purple)}
.search span{flex:1;background:#fff;color:#aaa;font-size:14px;padding:14px 16px}
.search b{width:52px;background:var(--yellow);display:flex;align-items:center;justify-content:center}
.hero .hint{position:absolute;left:40px;top:262px;font-size:11px;color:var(--muted)}
.hero-photo{position:absolute;left:640px;top:20px;width:300px;height:430px;background:linear-gradient(#dcdde2,#b9bcc6)}
.band{height:100px;background:var(--yellow)}
.band .wrap{display:flex;align-items:center;justify-content:space-between;padding:0 40px}
.band p{font-size:15px;font-weight:600;color:var(--purple);width:520px;line-height:1.45}
.btn-dark{background:var(--purple);color:#fff;font-size:14px;font-weight:600;padding:12px 34px}
.reasons{height:520px;text-align:center}
.reasons h3{padding-top:60px;font-size:30px;font-weight:700;color:var(--purple)}
.reasons .sub{font-size:14px;color:var(--muted);margin-top:6px}
.features{display:flex;justify-content:space-between;margin:46px 60px 0}
.feature{width:250px}
.feature .icon{width:70px;height:70px;margin:0 auto 18px;border:2px solid var(--purple);border-radius:50%;display:flex;align-items:center;justify-content:center}
.feature h4{font-size:15px;font-weight:600;color:var(--purple);margin-bottom:8px}
.feature p{font-size:11px;color:var(--muted);line-height:1.55}
.btn-yellow{display:inline-block;margin-top:50px;background:var(--yellow);color:var(--purple);font-weight:700;font-size:15px;padding:14px 36px}
.premium{height:440px;background:var(--soft);border-top:1px solid var(--line)}
.sign{position:absolute;left:40px;top:-12px;width:120px;height:170px;background:linear-gradient(#c7343a,#9a1f25)}
.premium h3{position:absolute;left:200px;top:34px;font-size:34px;font-weight:400;color:var(--purple)}
.premium .lead{position:absolute;left:200px;top:84px;width:720px;font-size:11px;color:var(--muted);line-height:1.5}
.offers{position:absolute;left:40px;top:150px;width:920px}
.offer{display:flex;align-items:center;height:56px;border-bottom:1px solid var(--line);background:#fff;margin-bottom:8px;padding:0 14px}
.offer .btn-sm{background:var(--yellow);color:var(--purple);font-weight:600;font-size:13px;padding:8px 20px}
.offer .name{flex:1;text-align:center;font-size:15px;font-weight:600;color:var(--purple);letter-spacing:.5px}
.offer .name span{font-weight:400;color:var(--muted)}
.offer .price{width:120px;text-align:right;font-weight:700;font-size:15px;color:var(--purple)}
.see{position:absolute;right:40px;top:412px;font-size:10px;color:var(--muted)}
.popular{height:500px}
.pop-photo{position:absolute;left:0;top:50px;width:190px;height:450px;background:linear-gradient(#e4e0e6,#c7bfcb)}
.pop-table{position:absolute;left:200px;top:50px;width:420px;background:#fff;border:1px solid var(--line)}
.pop-table h3{font-size:20px;font-weight:600;color:var(--purple);padding:16px 16px 10px}
.row{display:flex;font-size:12px;padding:9px 16px;border-top:1px solid var(--line)}
.row .d{flex:1}
.row .p{width:90px;color:var(--purple);font-weight:600}
.row .m{width:80px;color:var(--muted)}
.row .s{width:60px;text-align:right;color:var(--muted)}
.faq{position:absolute;left:650px;top:50px;width:350px}
.q{border:1px solid var(--line);margin-bottom:10px;font-size:13px;color:var(--muted)}
.q .t{padding:12px 14px;display:flex;gap:10px;align-items:center}
.q .t i{width:22px;height:22px;background:#ddd;color:#fff;font-style:normal;display:flex;align-items:center;justify-content:center;font-size:14px}
.q.open .t{color:var(--purple);font-weight:600}
.q.open .t i{background:var(--yellow);color:var(--purple)}
.q p{font-size:11px;line-height:1.55;padding:0 14px 14px 46px}
.footer{height:210px;background:var(--purple);color:#cbbfd3}
.cols{display:flex;justify-content:space-between;padding-top:30px}
.col{width:220px}
.col h5{color:#fff;font-size:14px;font-weight:600;border-bottom:1px solid #57385f;padding-bottom:6px;margin-bottom:8px}
.col li{list-style:none;font-size:11px;line-height:1.55}
.bottom{height:38px;background:var(--purple-deep);color:#9c8ca6;font-size:10px}
.bottom .wrap{display:flex;justify-content:space-between;align-items:center}
.social,.cards{display:flex;gap:6px}
.social span{width:14px;height:14px;border-radius:50%;background:#6d5577}
.cards span{width:30px;height:18px;background:#e9e4ec;border-radius:2px}
</style>
</head>
<body>
<div class="topbar"><div class="wrap"><span>Default welcome msg!</span><nav><span>My Account</span><span>Wish List</span><span>Checkout</span><span>Log In</span></nav></div></div>
<header class="header"><div class="wrap">
  <div class="brand">Lesyra Domains</div>
  <nav class="mainnav"><a class="active">Home</a><a>About</a><a>Pages</a><a>Blog</a><a>Support</a></nav>
</div></header>

<section class="hero"><div class="wrap">
  <h1>YOUR BUSINESS STARTS HERE</h1>
  <h2>BUY A PREMIUM DOMAIN AND OPEN YOUR DOORS</h2>
  <div class="search"><span>Enter Domain Name</span><b><svg width="20" height="20" viewBox="0 0 20 20"><circle cx="8" cy="8" r="6" fill="none" stroke="#351a41" stroke-width="2.5"/><line x1="12.5" y1="12.5" x2="18" y2="18" stroke="#351a41" stroke-width="2.5"/></svg></b></div>
  <p class="hint">Have an existing domain with another registrar? Start your transfer now</p>
  <div class="hero-photo" role="img" aria-label="Photo of a smiling businessman in a light shirt"></div>
</div></section>

<section class="band"><div class="wrap">
  <p>Do come and lease the best domain name you are interested in from Home &amp; Garden Category!</p>
  <span class="btn-dark">Find Lease Domains &rsaquo;</span>
</div></section>

<section class="reasons"><div class="wrap">
  <h3>REASONS YOU WILL LOVE LESYRA DOMAINS</h3>
  <p class="sub">We are committed to working with you to choose the best domain!</p>
  <div class="features">
    <div class="feature">
      <div class="icon"><svg width="34" height="34" viewBox="0 0 34 34" fill="none" stroke="#351a41" stroke-width="2"><circle cx="17" cy="17" r="13"/><ellipse cx="17" cy="17" rx="6" ry="13"/><line x1="4" y1="17" x2="30" y2="17"/></svg></div>
      <h4>Get your own web address</h4>
      <p>Amazingly simple search, registration and DNS management for 100+ international domain name extensions.</p>
    </div>
    <div class="feature">
      <div class="icon"><svg width="34" height="34" viewBox="0 0 34 34" fill="none" stroke="#351a41" stroke-width="2"><rect x="5" y="8" width="24" height="18" rx="2"/><line x1="11" y1="30" x2="23" y2="30"/></svg></div>
      <h4>The best apps for your domains</h4>
      <p>Quickly and easily add the best email, blog and website services to your domains in just one single click.</p>
    </div>
    <div class="feature">
      <div class="icon"><svg width="34" height="34" viewBox="0 0 34 34" fill="none" stroke="#351a41" stroke-width="2"><path d="M6 24l8-8 5 5 9-11"/><path d="M22 10h6v6"/></svg></div>
      <h4>A new world of domain names</h4>
      <p>Register your interest in hundreds of all new top level domains such as .APP, .BLOG, .CLUB, and .SHOP.</p>
    </div>
  </div>
  <span class="btn-yellow">SEE PLANS &amp; PRICING</span>
</div></section>

<section class="premium"><div class="wrap">
  <div class="sign" role="img" aria-label="Illustration of a red for-sale sign on a post"></div>
  <h3>Premium Domains</h3>
  <p class="lead">Lesyra has over six million available domain names ready to become businesses. Read the brief purchase below to explore how to start your own domain name search.</p>
  <div class="offers">
    <div class="offer"><span class="btn-sm">Make Offer</span><span class="name">RIVERSTEPS<span>.COM</span></span><span class="price">$2,088</span></div>
    <div class="offer"><span class="btn-sm">Make Offer</span><span class="name">BREEZEVAULT<span>.COM</span></span><span class="price">$2,088</span></div>
    <div class="offer"><span class="btn-sm">Make Offer</span><span class="name">DUNEHARBOR<span>.COM</span></span><span class="price">$2,088</span></div>
    <div class="offer"><span class="btn-sm">Make Offer</span><span class="name">MOTORBIDLANE<span>.COM</span></span><span class="price">$2,088</span></div>
  </div>
  <span class="see">See more</span>
</div></section>

<section class="popular"><div class="wrap">
  <div class="pop-photo" role="img" aria-label="Photo of a smiling businesswoman in a dark suit"></div>
  <div class="pop-table">
    <h3>Popular Domains</h3>
    <div class="row"><span class="d">Tavelcard.com</span><span class="p">$1550</span><span class="m">Make Offer</span><span class="s">Lease</span></div>
    <div class="row"><span class="d">Simmerly.com</span><span class="p">$1690</span><span class="m">Make Offer</span><span class="s">Lease</span></div>
    <div class="row"><span class="d">Fairwaxo.com</span><span class="p">$1180</span><span class="m">Make Offer</span><span class="s">Lease</span></div>
    <div class="row"><span class="d">Lumbrix.com</span><span class="p">$4450</span><span class="m">Make Offer</span><span class="s">Lease</span></div>
    <div class="row"><span class="d">Trovany.com</span><span class="p">$1880</span><span class="m">Make Offer</span><span class="s">Lease</span></div>
    <div class="row"><span class="d">Tavelcard.com</span><span class="p">$1550</span><span class="m">Make Offer</span><span class="s">Lease</span></div>
    <div class="row"><span class="d">See more</span><span class="p"></span><span class="m"></span><span class="s">94/309</span></div>
  </div>
  <div class="faq">
    <div class="q open"><div class="t"><i>&minus;</i>What is a premium domain name?</div>
      <p>The potential list of meaningful domains that are available for sale registered or becoming discoverable. Our domain has already sold. That means a premium domain name has been priced by owner and is ready to buy.</p></div>
    <div class="q"><div class="t"><i>+</i>If my password does not work?</div></div>
    <div class="q"><div class="t"><i>+</i>Who is Lesyra Domains?</div></div>
  </div>
</div></section>

<footer class="footer"><div class="wrap"><div class="cols">
  <div class="col"><h5>Categories</h5><ul><li>Automotive</li><li>Business and Finance</li><li>Computers and Internet</li><li>Education</li><li>Entertainment</li><li>Family</li><li>Food and Beverage</li></ul></div>
  <div class="col"><h5>About Us</h5><ul><li>Join our newsletter</li><li>About Us</li><li>Contact Us</li><li>Blog</li><li>Success Stories</li><li>Membership Contract</li><li>Privacy Policy</li></ul></div>
  <div class="col"><h5>Buy Domains</h5><ul><li>Premium Domains</li><li>Bargain Domains</li><li>Popular Domains</li><li>Top Keywords</li></ul></div>
  <div class="col"><h5>Contact Us</h5><ul><li>Norwell Ridge Homes C/o, Route 48</li><li>P.O. Box 270, Larkfield, ME 04199</li><li>207-555-0148</li><li>info@norwellridgehomes.com</li></ul></div>
</div></div></footer>
<div class="bottom"><div class="wrap">
  <span>Copyright Lesyra Domains. All rights reserved</span>
  <div class="social"><span></span><span></span><span></span><span></span><span></span></div>
  <div class="cards"><span></span><span></span><span></span><span></span><span></span></div>
</div></div>
</body>
</html>
```